Delvane Roofing Commercial Truck Wrap

Need to wrap new white truck, 2021 Marvane Ridgeline 3400 K48, 8 ft. bed. Our logo is red. We need to include the following: Logo, website DelvaneRoofing.example, phone number 555-318-4096, callout that we do Roofing, Siding, Gutters. Also Storm Damage Experts. Include Tallis Brandt Select Installer logo along with Blue Heron, Fair Trade Guild logo, callout that say Since 1962. Perhaps use a graphic that depicts a house with a roof in the background or something else that depicts roofs/homes. We plan on using Q7 product to wrap sides and back of truck. Also consider using back passenger windows on both side of truck. We are not going to wrap the hood, roof or back window. Thank you!

Requirements
Must have
• logo, phone number, website, tallis brandt logo and blue heron, callouts that we do roofing siding and gutters, in business since 1962
Nice to have
• We would like to be able to use the sides and tailgate of the truck for our messages. Would also like to be able to use passenger back windows for design as well. Maybe consider a graphic of a house or shingles or something roof related if it will enhance appeal of the design

```html
<!DOCTYPE html>
<html lang="en">
<head>
<meta charset="utf-8">
<title>Delvane Roofing – Truck Wrap Layout</title>
<link href="https://fonts.googleapis.com/css2?family=Montserrat:ital,wght@1,800&family=Open+Sans:wght@600;700&display=swap" rel="stylesheet">
<style>
  :root {
    --brand-red: #e2231a;
    --wrap-black: #141414;
    --wrap-white: #f4f4f4;
    --ink: #111111;
    --shingle-dark: #1f2a38;
    --shingle-light: #5a6b80;
    --worker-tone: #b89a6a;
    --badge-grey: #c9c9c9;
    --paper: #ffffff;
  }
  * { margin: 0; padding: 0; box-sizing: border-box; }
  html, body { width: 1200px; height: 1162px; overflow: hidden; background: var(--paper); }
  .canvas { position: relative; width: 1200px; height: 1162px; }
  .wrap-art { position: absolute; inset: 0; }
  .label { position: absolute; white-space: nowrap; line-height: 1; }

  .site { font-family: "Open Sans", sans-serif; font-weight: 600; color: var(--ink); }
  .site--light { color: var(--wrap-white); }
  .since { font-family: "Open Sans", sans-serif; font-weight: 600; color: var(--brand-red); }
  .since--light { color: var(--wrap-white); }
  .brand-name { font-family: "Open Sans", sans-serif; font-weight: 700; color: var(--ink); letter-spacing: -0.5px; }
  .brand-name--light { color: var(--wrap-white); }
  .brand-sub { font-family: "Open Sans", sans-serif; font-weight: 700; color: var(--ink); letter-spacing: 6px; }
  .brand-sub--light { color: var(--wrap-white); }
  .callout {
    font-family: "Montserrat", sans-serif; font-style: italic; font-weight: 800;
    color: var(--brand-red); text-transform: uppercase;
    text-shadow: -1px -1px 0 #fff, 1px -1px 0 #fff, -1px 1px 0 #fff, 1px 1px 0 #fff;
  }
  .phone { font-family: "Montserrat", sans-serif; font-style: italic; font-weight: 800; color: var(--wrap-white); }
</style>
</head>
<body>
<main class="canvas">
  <svg class="wrap-art" width="1200" height="1162" viewBox="0 0 1200 1162">
    <defs>
      <linearGradient id="shingleTone" x1="0" y1="1" x2="1" y2="0">
        <stop offset="0" stop-color="var(--shingle-light)"/>
        <stop offset="1" stop-color="var(--shingle-dark)"/>
      </linearGradient>
      <linearGradient id="workerTone" x1="0" y1="0" x2="0" y2="1">
        <stop offset="0" stop-color="#d8c08a"/>
        <stop offset="1" stop-color="var(--worker-tone)"/>
      </linearGradient>
    </defs>

    <!-- side panel -->
    <g class="side-panel">
      <rect x="34" y="130" width="720" height="265" fill="var(--wrap-white)"/>
      <polygon points="535,395 535,262 740,130 754,130 754,395" fill="var(--brand-red)"/>
      <rect x="754" y="212" width="410" height="183" fill="var(--wrap-black)"/>
      <polygon points="790,230 1150,212 1150,275 830,275" fill="var(--brand-red)"/>
      <polygon role="img" aria-label="Photo of roof shingles" points="500,395 640,300 760,222 850,212 900,212 780,300 760,395" fill="url(#shingleTone)"/>
      <rect role="img" aria-label="Photo of a roofer at work on a roof" x="655" y="170" width="92" height="118" fill="url(#workerTone)"/>
      <rect class="badge" x="555" y="196" width="10" height="14" fill="var(--badge-grey)"/>
      <rect class="badge" x="570" y="197" width="38" height="12" fill="var(--badge-grey)"/>
      <rect x="336" y="258" width="12" height="12" fill="var(--brand-red)"/>
    </g>

    <!-- tailgate panel -->
    <g class="tailgate-panel">
      <rect x="352" y="673" width="542" height="184" fill="var(--wrap-black)"/>
      <rect x="352" y="727" width="490" height="44" fill="var(--brand-red)"/>
      <polygon role="img" aria-label="Photo of roof shingles" points="540,820 650,772 842,772 842,820" fill="url(#shingleTone)"/>
    </g>
  </svg>

  <!-- side texts -->
  <span class="label site" style="left:555px;top:146px;font-size:12px;">delvaneroofing.example</span>
  <span class="label since" style="left:568px;top:164px;font-size:15px;">Since 1962</span>
  <span class="label brand-name" style="left:354px;top:252px;font-size:34px;">Delvane</span>
  <span class="label brand-sub" style="left:338px;top:298px;font-size:11px;">Roofing Inc.</span>
  <span class="label callout" style="left:590px;top:290px;font-size:19px;">Roofing</span>
  <span class="label callout" style="left:588px;top:316px;font-size:19px;">Siding</span>
  <span class="label callout" style="left:590px;top:342px;font-size:19px;">Gutters</span>
  <span class="label callout" style="left:822px;top:224px;font-size:19px;">Storm Damage Expert</span>
  <span class="label phone" style="left:912px;top:250px;font-size:23px;">555-318-4096</span>

  <!-- tailgate texts -->
  <span class="label site site--light" style="left:665px;top:700px;font-size:15px;">delvaneroofing.example</span>
  <span class="label brand-name brand-name--light" style="left:416px;top:728px;font-size:36px;">Delvane</span>
  <span class="label brand-sub brand-sub--light" style="left:418px;top:776px;font-size:11px;">Roofing Inc.</span>
  <span class="label phone" style="left:630px;top:737px;font-size:25px;">555-318-4096</span>
  <span class="label since since--light" style="left:700px;top:795px;font-size:18px;">Since 1962</span>
  <span class="label callout" style="left:425px;top:825px;font-size:22px;">Roofing | Siding | Gutters</span>
</main>
</body>
</html>
```